Hi Designers,

I will need 4 web pages designed. The web page looks like an App (if you click on the logo, or the icon on an iPad, it will take you to the website), but it is still a webpage.

Please check the attachment on this brief to understand what specific pages I need to be designed.

A .PSD (straight-up PhotoShop image) as final deliverable is fine, as long as you give us the exact “web color numbers”.

The design is for desktop and iPad but in a single unified web application, NOT separate web app and (native) iPad app.

Details:

Brightwell Ledger Advisory Group is developing a browser-based application for use on any mobile device or desktop. The app will be used by corporations to communicate with their employees regarding legal, regulatory and company requirements for conducting business. The app is known as “Harbor Rulebook Hub.” When the user clicks on the icon for Harbor Rulebook Hub, they will enter a site full of information that a company deems necessary for the employee to do his/her job. There are several content sections within the site, including a login page, training, policies, forms, news feeds and blogs.

The application has been built using Microsoft .NET, and fully supports CSS-type skinning; it uses traditional page layouts. We are seeking a product logo concept (image), a master application/desktop icon (image), as well as a full color scheme/theme/skin design for all areas of the application (header area, body text, menu bar, etc.) in the form of a CSS. The look should be clean, crisp and professional; nothing cartoony or whimsical. It should be easy to read and “airy”.

We have sketched prototypes for the basic application page layout that we can send as a next step of the process.
Updates

Screen shots have been uploaded to this project.  Please use them to guide your design.

Dear designers,

I apologize for the delay in providing feedback. My partners and I will provide feedback in a few days. Thank you for your patience.

Industry/Entity Type

Business

Font styles to use
Other font styles liked:
• see font on screen shots when uploaded

```html
<!DOCTYPE html>
<html lang="en">
<head>
<meta charset="utf-8">
<title>Harbor Rulebook Hub</title>
<link rel="stylesheet" href="https://fonts.googleapis.com/css2?family=Signika:wght@300;400;600&display=swap">
<style>
:root{
  --bg:#f1f2f4;
  --bar:#e3e3e3;
  --bar-line:#cfcfcf;
  --panel:#ffffff;
  --text:#444;
  --muted:#6d6d6d;
  --grey-head:#a9a9a9;
  --dark-head:#8c8c8c;
  --red:#f0625f;
  --teal:#5bd8bd;
  --teal-text:#3fbf9f;
  --blue:#5cc8ef;
  --link:#2aa3d6;
  --card:#f5f5f5;
  --row-a:#d8d8d8;
  --row-b:#cdcdcd;
  --thumb:#8d9aa6;
}
*{box-sizing:border-box;margin:0;padding:0}
html,body{width:1200px;height:900px;overflow:hidden}
body{background:var(--bg);font-family:"Signika",sans-serif;color:var(--text)}
.app{width:1200px;height:900px;display:flex;flex-direction:column}

/* top bar */
.topbar{height:60px;background:var(--bar);display:flex;border-bottom:1px solid var(--bar-line)}
.tab{width:140px;display:flex;align-items:center;justify-content:center;border-right:1px solid var(--bar-line);position:relative}
.tab:first-child{background:#d6d6d6}
.tab svg{width:38px;height:34px;fill:none;stroke:#9a9a9a;stroke-width:2.4}
.badge{position:absolute;top:10px;left:78px;background:var(--red);color:#fff;font-size:12px;font-weight:600;width:18px;height:18px;border-radius:3px;display:flex;align-items:center;justify-content:center}
.user{margin-left:auto;display:flex;align-items:center;gap:16px;padding-right:48px;font-size:15px;color:#555}
.avatar{width:38px;height:40px;background:linear-gradient(#c9d3dc,#7a8794)}
.caret{width:0;height:0;border-left:6px solid transparent;border-right:6px solid transparent;border-top:7px solid #777}

.main{flex:1;display:grid;grid-template-columns:246px 1fr 260px;gap:6px;padding:4px 0 0 0;min-height:0}

/* panel headings */
.head{display:flex;align-items:center;gap:12px;height:40px;padding:0 16px;color:#fff;font-size:17px}
.head svg{width:18px;height:18px}

/* industry news */
.news{background:var(--panel);display:flex;flex-direction:column}
.news .head{background:var(--grey-head)}
.search{margin:12px 12px 14px;height:30px;border:1px solid #c9c9c9;border-radius:6px;display:flex;align-items:center;gap:8px;padding:0 10px;font-size:12px;color:#aaa}
.search svg{width:12px;height:12px;stroke:#aaa;fill:none;stroke-width:2}
.news-item{display:flex;gap:18px;padding:20px 14px 0 14px;height:171px;border-bottom:1px solid #e6e6e6}
.news-item.active{background:var(--card);border-left:4px solid var(--red);padding-left:10px}
.news-item:nth-child(odd){}
.date{width:26px;text-align:center;font-size:9px;color:#777;flex:none}
.date svg{width:26px;height:28px;display:block}
.news-body{font-size:12.5px;line-height:1.45;color:#555}
.news-body a{display:inline-block;margin-top:14px;color:var(--link);font-size:12px;text-decoration:underline}

/* centre */
.centre{display:flex;flex-direction:column;gap:12px;padding-top:4px}
.welcome{background:var(--panel);margin-right:4px}
.welcome .head{background:var(--red)}
.welcome-body{display:flex;gap:26px;padding:14px 20px 12px}
.portrait{width:94px;height:86px;flex:none;background:linear-gradient(#d8c4a0,#8c7a66)}
.welcome-body p{font-size:12.5px;line-height:1.5;color:#555;padding-top:8px}
.cols{display:grid;grid-template-columns:1fr 1fr;gap:16px;flex:1;padding:0 4px 0 8px;min-height:0}
.feed .head{background:var(--teal)}
.games .head{background:var(--blue)}
.feed-list{background:var(--panel);height:612px;padding:4px 18px}
.feed-item{display:flex;gap:18px;align-items:center;height:96px;border-bottom:1px solid #e6e6e6}
.feed-item:last-child{border-bottom:0}
.thumb{width:58px;height:42px;flex:none;background:linear-gradient(#dfe5ea,var(--thumb))}
.feed-item .when{color:var(--teal-text);font-size:13px;margin-bottom:4px}
.feed-item p{font-size:12px;line-height:1.45;color:#555}
.game-list{background:var(--panel);height:612px;padding:10px 10px 0}
.game{background:var(--card);height:130px;margin-bottom:22px;display:flex;gap:22px;padding:22px 16px;border-bottom:4px solid #d9d9d9}
.game svg{width:34px;height:34px;flex:none;stroke:var(--blue);fill:none;stroke-width:2}
.game h3{font-weight:400;font-size:16px;color:#555;margin-bottom:8px}
.game p{font-size:12px;line-height:1.45;color:#555}

/* leaderboard */
.board{background:var(--row-a);display:flex;flex-direction:column;padding-top:4px}
.board .head{background:var(--dark-head);justify-content:flex-start;padding-left:34px}
.board table{width:100%;border-collapse:collapse;font-size:12px;color:#444}
.board th{font-weight:400;color:#777;background:#eeeeee;height:36px;font-size:11.5px;text-align:left}
.board td{height:31px}
.board td:first-child,.board th:first-child{padding-left:12px;width:46px}
.board td:nth-child(3),.board th:nth-child(3){width:58px}
.board tr.top td{background:#fff;height:48px}
.board tbody tr:nth-child(even) td{background:var(--row-a)}
.board tbody tr:nth-child(odd):not(.top) td{background:var(--row-b)}
.rank{display:inline-flex;width:13px;height:13px;border-radius:50%;background:#f3f3f3;border:1px solid #bbb;font-size:8px;align-items:center;justify-content:center}
</style>
</head>
<body>
<div class="app">
  <header class="topbar">
    <div class="tab"><svg viewBox="0 0 38 34"><path d="M4 17 19 4l15 13M9 13v17h20V13"/></svg><span class="badge">5</span></div>
    <div class="tab"><svg viewBox="0 0 38 34"><rect x="5" y="4" width="26" height="26"/><path d="M10 11h16M10 17h16M10 23h10"/></svg></div>
    <div class="tab"><svg viewBox="0 0 38 34"><rect x="4" y="4" width="30" height="20"/><path d="M19 24v6M12 30h14"/></svg></div>
    <div class="tab"><svg viewBox="0 0 38 34"><path d="M9 15a10 10 0 0 1 18-5l3 3M29 19a10 10 0 0 1-18 5l-3-3M30 6v7h-7M8 28v-7h7"/></svg></div>
    <div class="user"><div class="avatar" role="img" aria-label="User profile photo"></div><span>Daniel Harrow</span><span class="caret"></span></div>
  </header>

  <main class="main">
    <section class="news">
      <div class="head"><svg viewBox="0 0 18 18" fill="none" stroke="#fff" stroke-width="2"><rect x="2" y="3" width="13" height="13"/><path d="M7 11l8-8"/></svg>Industry news</div>
      <div class="search"><svg viewBox="0 0 12 12"><circle cx="5" cy="5" r="4"/><path d="M8 8l3 3"/></svg>Search news...</div>
      <article class="news-item">
        <div class="date"><svg viewBox="0 0 26 28" fill="none" stroke="#999" stroke-width="1.5"><rect x="2" y="4" width="22" height="22"/><path d="M2 10h22M8 2v5M18 2v5"/><text x="13" y="22" font-size="10" text-anchor="middle" fill="#777" stroke="none">28</text></svg>oct</div>
        <div class="news-body">Lorem ipsum dolor sit amet, ad tus inani vocibus. An nam possim fastidii, usu in fuisset dissentias, nec at persius denique<br><a>monthly report major's office</a></div>
      </article>
      <article class="news-item active">
        <div class="date"><svg viewBox="0 0 26 28" fill="none" stroke="#999" stroke-width="1.5"><rect x="2" y="4" width="22" height="22"/><path d="M2 10h22M8 2v5M18 2v5"/><text x="13" y="22" font-size="10" text-anchor="middle" fill="#777" stroke="none">28</text></svg>oct</div>
        <div class="news-body">Lorem ipsum dolor sit amet, ad tus inani vocibus. An nam possim fastidii, usu in fuisset dissentias, nec at persius denique<br><a>monthly report major's office</a></div>
      </article>
      <article class="news-item">
        <div class="date"><svg viewBox="0 0 26 28" fill="none" stroke="#999" stroke-width="1.5"><rect x="2" y="4" width="22" height="22"/><path d="M2 10h22M8 2v5M18 2v5"/><text x="13" y="22" font-size="10" text-anchor="middle" fill="#777" stroke="none">28</text></svg>oct</div>
        <div class="news-body">Lorem ipsum dolor sit amet, ad tus inani vocibus. An nam possim fastidii, usu in fuisset dissentias, nec at persius denique<br><a>monthly report major's office</a></div>
      </article>
      <article class="news-item" style="border-bottom:0">
        <div class="date"><svg viewBox="0 0 26 28" fill="none" stroke="#999" stroke-width="1.5"><rect x="2" y="4" width="22" height="22"/><path d="M2 10h22M8 2v5M18 2v5"/><text x="13" y="22" font-size="10" text-anchor="middle" fill="#777" stroke="none">28</text></svg>oct</div>
        <div class="news-body">Lorem ipsum dolor sit amet, ad tus inani vocibus. An nam possim fastidii, usu in fuisset dissentias, nec at persius denique<br><a>monthly report major's office</a></div>
      </article>
    </section>

    <section class="centre">
      <div class="welcome">
        <div class="head"><svg viewBox="0 0 18 18" fill="#fff"><path d="M9 1l2.4 5.3 5.6.6-4.2 3.8 1.2 5.6L9 13.4l-5 2.9 1.2-5.6L1 6.9l5.6-.6z"/></svg>Welcome to Harbor Rulebook Hub</div>
        <div class="welcome-body">
          <div class="portrait" role="img" aria-label="Photo of a community host"></div>
          <p>Lorem ipsum dolor sit amet, eu vix summo primis qualisque. Usu nihil atomorum eu, pri quod modo nemore cu, cu graeco perfecto vis. Ex est idque facilisis, ida intellegebat ius an, his te duis maiorum moderatius. Delicata necessitatibus mei in, mel</p>
        </div>
      </div>

      <div class="cols">
        <div class="feed">
          <div class="head"><svg viewBox="0 0 18 18" fill="#fff"><path d="M9 2C4.6 2 1 4.9 1 8.4c0 2 1.1 3.7 2.9 4.9L3 17l4-2.3c.6.1 1.3.2 2 .2 4.4 0 8-2.9 8-6.5S13.4 2 9 2z"/></svg>What's new</div>
          <div class="feed-list">
            <div class="feed-item"><div class="thumb" role="img" aria-label="News photo thumbnail"></div><div><div class="when">11/11/2013</div><p>Prompta civibus gloriatur mea te, an cum facete suavitate, ei vim corrumpit</p></div></div>
            <div class="feed-item"><div class="thumb" role="img" aria-label="News photo thumbnail"></div><div><div class="when">11/11/2013</div><p>Prompta civibus gloriatur mea te, an cum facete suavitate, ei vim corrumpit</p></div></div>
            <div class="feed-item"><div class="thumb" role="img" aria-label="News photo thumbnail"></div><div><div class="when">11/11/2013</div><p>Prompta civibus gloriatur mea te, an cum facete suavitate, ei vim corrumpit</p></div></div>
            <div class="feed-item"><div class="thumb" role="img" aria-label="News photo thumbnail"></div><div><div class="when">11/11/2013</div><p>Prompta civibus gloriatur mea te, an cum facete suavitate, ei vim corrumpit</p></div></div>
            <div class="feed-item"><div class="thumb" role="img" aria-label="News photo thumbnail"></div><div><div class="when">11/11/2013</div><p>Prompta civibus gloriatur mea te, an cum facete suavitate, ei vim corrumpit</p></div></div>
            <div class="feed-item"><div class="thumb" role="img" aria-label="News photo thumbnail"></div><div><div class="when">11/11/2013</div><p>Prompta civibus gloriatur mea te, an cum facete suavitate, ei vim corrumpit</p></div></div>
          </div>
        </div>

        <div class="games">
          <div class="head"><svg viewBox="0 0 18 18" fill="#fff"><circle cx="9" cy="5" r="4"/><path d="M1 17c0-4.4 3.6-7 8-7s8 2.6 8 7z"/></svg>Compliance game center</div>
          <div class="game-list">
            <div class="game"><svg viewBox="0 0 34 34"><circle cx="17" cy="15" r="11"/><circle cx="17" cy="13" r="4"/><path d="M10 24c2-4 12-4 14 0"/></svg><div><h3>Use Preferances</h3><p>Lorem ipsum dolor sit amet, ad tus inani vocibus. An nam possim fastidii, usu in fuisset dissentias,</p></div></div>
            <div class="game"><svg viewBox="0 0 34 34"><rect x="3" y="6" width="28" height="18"/><path d="M8 12h18M8 17h10M18 28l8-8 3 3-8 8h-3z"/></svg><div><h3>Real Time Updates</h3><p>Lorem ipsum dolor sit amet, ad tus inani vocibus. An nam possim fastidii, usu in fuisset dissentias,</p></div></div>
            <div class="game"><svg viewBox="0 0 34 34"><rect x="7" y="4" width="20" height="26"/><path d="M11 11h2M16 11h7M11 17h2M16 17h7M11 23h2M16 23h7"/></svg><div><h3>Team Standings</h3><p>Lorem ipsum dolor sit amet, ad tus inani vocibus. An nam possim fastidii, usu in fuisset dissentias,</p></div></div>
            <div class="game"><svg viewBox="0 0 34 34"><path d="M12 22a8 8 0 1 1 10 0v4H12zM13 30h8M17 2v2M5 12H3M31 12h-2M8 5l2 2M26 5l-2 2"/></svg><div><h3>Earn Bonus Points</h3><p>Lorem ipsum dolor sit amet, ad tus inani vocibus. An nam possim fastidii, usu in fuisset dissentias,</p></div></div>
          </div>
        </div>
      </div>
    </section>

    <aside class="board">
      <div class="head">Leaderboard</div>
      <table>
        <thead><tr><th>rank</th><th>player</th><th>%</th><th>score</th></tr></thead>
        <tbody>
          <tr class="top"><td><span class="rank">1</span></td><td>Morgan, L</td><td>92%</td><td>5093</td></tr>
          <tr><td><span class="rank">2</span></td><td>Avery, D</td><td>91%</td><td>5029</td></tr>
          <tr><td><span class="rank">3</span></td><td>Morgan, L</td><td>92%</td><td>5093</td></tr>
          <tr><td><span class="rank">2</span></td><td>Avery, D</td><td>91%</td><td>5029</td></tr>
          <tr><td><span class="rank">3</span></td><td>Morgan, L</td><td>92%</td><td>5093</td></tr>
          <tr><td><span class="rank">3</span></td><td>Morgan, L</td><td>92%</td><td>5093</td></tr>
          <tr><td><span class="rank">2</span></td><td>Avery, D</td><td>91%</td><td>5029</td></tr>
          <tr><td><span class="rank">3</span></td><td>Morgan, L</td><td>92%</td><td>5093</td></tr>
          <tr><td><span class="rank">3</span></td><td>Avery, D</td><td>91%</td><td>5029</td></tr>
          <tr><td><span class="rank">3</span></td><td>Morgan, L</td><td>92%</td><td>5093</td></tr>
          <tr><td><span class="rank">2</span></td><td>Morgan, L</td><td>92%</td><td>5093</td></tr>
          <tr><td><span class="rank">3</span></td><td>Morgan, L</td><td>92%</td><td>5093</td></tr>
          <tr><td><span class="rank">2</span></td><td>Avery, D</td><td>91%</td><td>5029</td></tr>
          <tr><td><span class="rank">2</span></td><td>Avery, D</td><td>91%</td><td>5029</td></tr>
          <tr><td><span class="rank">3</span></td><td>Morgan, L</td><td>92%</td><td>5093</td></tr>
          <tr><td><span class="rank">2</span></td><td>Avery, D</td><td>91%</td><td>5029</td></tr>
          <tr><td><span class="rank">3</span></td><td>Morgan, L</td><td>92%</td><td>5093</td></tr>
          <tr><td><span class="rank">2</span></td><td>Avery, D</td><td>91%</td><td>5029</td></tr>
          <tr><td><span class="rank">3</span></td><td>Morgan, L</td><td>92%</td><td>5093</td></tr>
          <tr><td><span class="rank">3</span></td><td>Avery, D</td><td>91%</td><td>5029</td></tr>
          <tr><td><span class="rank">3</span></td><td>Morgan, L</td><td>92%</td><td>5093</td></tr>
          <tr><td><span class="rank">2</span></td><td>Avery, D</td><td>91%</td><td>5029</td></tr>
          <tr><td><span class="rank">3</span></td><td>Morgan, L</td><td>92%</td><td>5093</td></tr>
        </tbody>
      </table>
    </aside>
  </main>
</div>
</body>
</html>
```